Business Card for Freelance Copywriting & Web Design Business

Hi! I have a logo but want a new business card. Here's a better idea of what I'm thinking:
-Brand new double-sided business card, rounded cards, embossed logo, nice quality paper
-Include phone (604-382-9145), email (hello@linnearowatt.org), and website (www.linnearowatt.org). No address, please, since I service clients worldwide.
-I'd like the fonts to match those on my website (www.linnearowatt.org). I had to purchase the one font (Born Ready), attached. I'm not sure which version was used on my site so I included all that I purchased. The secondary font is Helvetica
-I'd also like the tagline "Powerful Words. Impressive Results." included.
-My primary brand colour is the teal, colour #19ADC3
Linnea Rowatt | Linnea Rowatt Copywriting & Web Design <hello@linnearowatt.org>
-I'd also like the following services listed on the new cards:
SEO Website Content
SEO Blog Content
SEO Website Design
Contact Information for Business Card
as stated in brief
Font styles to use
Other font styles liked:
- See brief
Look and feel
Each slider illustrates characteristics of the customer's brand and the style your logo design should communicate.

```html
<!DOCTYPE html>
<html lang="en">
<head>
<meta charset="utf-8">
<title>Linnea Rowatt Copywriting &amp; Web Design – Business Card</title>
<link href="https://fonts.googleapis.com/css2?family=Montserrat:wght@400;500;600;700&display=swap" rel="stylesheet">
<style>
  :root {
    --stage: #2b2b2b;
    --card-dark: #1b1b1b;
    --card-light: #ffffff;
    --teal: #19adc3;
    --feather: #8fc6d3;
    --feather-deep: #6fb0bf;
    --ink: #1a1a1a;
    --mark-dim: #5a5a5a;
    --white: #ffffff;
  }
  * { box-sizing: border-box; margin: 0; padding: 0; }
  html, body {
    width: 1200px; height: 905px; overflow: hidden;
    background: var(--stage);
    font-family: "Montserrat", Helvetica, Arial, sans-serif;
  }
  .stage {
    position: relative; width: 1200px; height: 905px;
    display: flex; flex-direction: column; align-items: center; justify-content: center; gap: 44px;
  }
  .card {
    position: relative; width: 640px; height: 366px; border-radius: 22px; overflow: hidden;
    box-shadow: 0 10px 30px rgba(0,0,0,.45);
  }

  /* Back */
  .card--back { background: var(--card-dark); }
  .card--back .brand {
    position: absolute; left: 0; right: 0; top: 112px; text-align: center;
    color: var(--mark-dim); font-weight: 600;
  }
  .brand__name { display: block; font-size: 44px; letter-spacing: 1px; }
  .brand__line { display: block; font-size: 15px; letter-spacing: 5px; text-transform: uppercase; margin-top: 8px; }
  .services {
    position: absolute; left: 0; right: 0; bottom: 42px;
    display: flex; justify-content: center; align-items: center; gap: 12px;
    color: var(--white); font-size: 15px; font-weight: 400; letter-spacing: .4px;
  }
  .services__dot { width: 6px; height: 6px; border-radius: 50%; background: var(--teal); }

  /* Front */
  .card--front { background: var(--card-light); }
  .card--front .brand {
    position: absolute; left: 50px; top: 60px; color: var(--teal); font-weight: 600;
  }
  .card--front .brand__name { font-size: 38px; }
  .card--front .brand__line { font-size: 12px; letter-spacing: 3.5px; margin-top: 6px; }
  .tagline {
    position: absolute; left: 64px; top: 182px; width: 300px; color: var(--ink);
    font-size: 14px; font-weight: 500; line-height: 1.4;
  }
  .contact {
    position: absolute; left: 64px; top: 246px; list-style: none;
    color: var(--ink); font-size: 14.5px;
  }
  .contact__item { display: flex; align-items: center; gap: 12px; height: 26px; }
  .contact__icon { width: 15px; height: 15px; flex: none; }
  .feather-art {
    position: absolute; right: 34px; top: 34px; width: 190px; height: 290px;
    border-radius: 60% 40% 55% 45% / 30% 30% 70% 70%;
    background: radial-gradient(ellipse at 45% 35%, var(--feather) 0%, var(--feather-deep) 70%, rgba(111,176,191,.5) 100%);
    transform: rotate(18deg); opacity: .85;
  }
</style>
</head>
<body>
<main class="stage">

  <section class="card card--back" aria-label="Business card back">
    <div class="brand">
      <span class="brand__name">Linnea Rowatt</span>
      <span class="brand__line">Copywriting &amp; Web Design</span>
    </div>
    <div class="services">
      <span>SEO Website Content</span>
      <span class="services__dot"></span>
      <span>SEO Blog Content</span>
      <span class="services__dot"></span>
      <span>SEO Website Design</span>
    </div>
  </section>

  <section class="card card--front" aria-label="Business card front">
    <div class="brand">
      <span class="brand__name">Linnea Rowatt</span>
      <span class="brand__line">Copywriting &amp; Web Design</span>
    </div>

    <p class="tagline">Powerful Words. Impressive Results.</p>

    <ul class="contact">
      <li class="contact__item">
        <svg class="contact__icon" viewBox="0 0 24 24" aria-hidden="true"><path fill="var(--teal)" d="M6.6 10.8a15.5 15.5 0 0 0 6.6 6.6l2.2-2.2a1 1 0 0 1 1-.25 11.4 11.4 0 0 0 3.6.57 1 1 0 0 1 1 1V20a1 1 0 0 1-1 1A17 17 0 0 1 3 4a1 1 0 0 1 1-1h3.5a1 1 0 0 1 1 1c0 1.250.2 2.450.57 3.6a1 1 0 0 1-.25 1z"/></svg>
        <span>604-382-9145</span>
      </li>
      <li class="contact__item">
        <svg class="contact__icon" viewBox="0 0 24 24" aria-hidden="true"><rect x="2" y="5" width="20" height="14" rx="2" fill="var(--teal)"/><path d="M3 6l9 7 9-7" fill="none" stroke="#fff" stroke-width="1.6"/></svg>
        <span>hello@linnearowatt.org</span>
      </li>
      <li class="contact__item">
        <svg class="contact__icon" viewBox="0 0 24 24" aria-hidden="true"><g fill="none" stroke="var(--teal)" stroke-width="2"><circle cx="12" cy="12" r="9.5"/><ellipse cx="12" cy="12" rx="4.2" ry="9.5"/><path d="M2.5 12h19M4 7h16M4 17h16"/></g></svg>
        <span>www.linnearowatt.org</span>
      </li>
    </ul>

    <div class="feather-art" role="img" aria-label="Large pale teal feather illustration"></div>
  </section>

</main>
</body>
</html>
```